BEACON CABS

Taxi card design

Need changes very slow in replying to my messages.

Target Market(s)

Customers

Industry/Entity Type

Taxi

Contact Information for Business Card

See previous design

Font styles to use
Sans Serif

Colors
A7469A
B969AE
D3A5CF
EDDBEB
F8F0F9
6B429C
8869AF
B7A5CE
E3DAEB
F3F0F8

Requirements
Nice to have
• We are in the business of looking after people, not just driving vehicles front
Should not have
• Front number 01632 480 480 needs to big big

```html
<!DOCTYPE html>
<html lang="en">
<head>
<meta charset="utf-8">
<title>Beacon Cabs – Business Card</title>
<link href="https://fonts.googleapis.com/css2?family=Bebas+Neue&family=Questrial&display=swap" rel="stylesheet">
<style>
  :root{
    --page:#ffffff;
    --card:#f1eef5;
    --ink:#0d0b10;
    --white:#ffffff;
    --deep:#2b0562;
    --mid:#6b1079;
    --magenta:#a81882;
    --violet:#6b429c;
    --lilac:#8869af;
  }
  *{box-sizing:border-box;margin:0;padding:0}
  html,body{width:1200px;height:720px;overflow:hidden;background:var(--page)}
  .card{position:absolute;left:40px;top:40px;width:1120px;height:640px;background:var(--card);overflow:hidden}
  .display{font-family:"Bebas Neue",Impact,sans-serif;line-height:1}
  .body-text{font-family:"Questrial",Arial,sans-serif}

  .established{position:absolute;left:83px;top:60px;font-size:28px;letter-spacing:3.4px;color:var(--ink)}

  .phone-icon{position:absolute;left:450px;top:67px;width:38px;height:51px}
  .main-number{position:absolute;left:503px;top:61px;width:524px;height:66px;
    display:flex;justify-content:space-between;font-size:66px;color:var(--ink);white-space:nowrap}
  .main-number .group{display:flex;gap:0}
  .main-number .group-area{width:186px;display:flex;justify-content:space-between}
  .main-number .group-line{width:110px;display:flex;justify-content:space-between}
  .handset-bracket{position:absolute;left:1044px;top:67px;width:32px;height:100px}

  .number-band{position:absolute;left:489px;top:135px;width:538px;height:33px;border-radius:16px 0 0 16px;
    background:linear-gradient(90deg,var(--magenta),var(--mid) 55%,var(--deep));
    display:flex;justify-content:space-between;align-items:center;padding:2px 10px 0 16px}
  .number-band span{font-size:23px;letter-spacing:1.6px;color:var(--white)}

  .service-tab{position:absolute;left:74px;width:324px;height:67px;
    border-radius:0 45px 0 45px;
    background:linear-gradient(100deg,var(--deep),var(--mid) 50%,var(--magenta));
    display:flex;align-items:center;justify-content:center;padding-top:4px;
    font-size:35px;letter-spacing:0.6px;color:var(--white)}
  .tab-airport{top:208px}
  .tab-minibus{top:321px}
  .tab-school{top:428px}

  .corner-shape{position:absolute;left:0;top:542px;width:200px;height:98px;border-radius:0 100px 0 0 / 0 70px 0 0;
    background:linear-gradient(90deg,var(--mid),var(--magenta))}

  .brand-name{position:absolute;left:509px;top:268px;width:444px;text-align:center;font-size:78px;letter-spacing:6px;color:var(--ink)}
  .hours{position:absolute;left:696px;top:370px;font-size:46px;letter-spacing:5.4px;color:var(--ink)}

  .contact,.address{position:absolute;font-size:17px;letter-spacing:1.6px;line-height:21.5px;color:var(--ink)}
  .contact{left:476px;top:524px}
  .address{left:845px;top:502px}
</style>
</head>
<body>
<div class="card">
  <p class="established display">Established since 1986</p>

  <svg class="phone-icon" viewBox="0 0 38 51" aria-hidden="true">
    <path d="M6 2 L12 0 L19 14 L14 18 Q18 30 26 38 L31 34 L38 44 L34 50 Q26 52 16 42 Q2 26 2 10 Z" fill="var(--violet)"/>
    <path d="M14 18 Q18 30 26 38 L31 34 L38 44 L34 50 Q26 52 16 42 Z" fill="var(--lilac)"/>
  </svg>
  <p class="main-number display" aria-label="01632 480 480">
    <span class="group-area"><span>0</span><span>1</span><span>6</span><span>3</span><span>2</span></span>
    <span class="group-line"><span>4</span><span>8</span><span>0</span></span>
    <span class="group-line"><span>4</span><span>8</span><span>0</span></span>
  </p>
  <svg class="handset-bracket" viewBox="0 0 32 100" aria-hidden="true">
    <defs>
      <linearGradient id="bracketFill" x1="0" y1="0" x2="0" y2="1">
        <stop offset="0" stop-color="#a81882"/>
        <stop offset="1" stop-color="#3a0868"/>
      </linearGradient>
    </defs>
    <path d="M0 0 H10 Q32 2 32 50 Q32 98 10 100 H0 V68 H10 V34 H0 Z" fill="url(#bracketFill)"/>
  </svg>
  <div class="number-band display">
    <span>01632 96 06 66</span>
    <span>01632 96 02 20</span>
    <span>01632 96 08 11</span>
  </div>

  <div class="service-tab tab-airport display">Airport Transfers</div>
  <div class="service-tab tab-minibus display">Mini Buses</div>
  <div class="service-tab tab-school display">School Transport</div>

  <div class="corner-shape"></div>

  <p class="brand-name display">Beacon Cabs</p>
  <p class="hours display">24/7 Services</p>

  <p class="contact body-text">
    Freephone: 0808 157 0 222<br>
    Email: hello@beaconcabs.co.uk<br>
    Website: www.beaconcabs.co.uk
  </p>
  <p class="address body-text">
    St Marys Parish Hall<br>
    Harbour Row<br>
    Eastbridge<br>
    EB4 7QT
  </p>
</div>
</body>
</html>
```